Catalog Design for herbal supplement products

We need a product catalog for several of our new dietary supplement products. We specialize in herbal formula, so we want our catalog to have some pictures of herbs, greens, flowers, plants for nature's feeling. We would like to see the catalog matches the color of our logo ( attached file). We need a text area with clear, readable fond and size for product description.

P.S.: I just upload another file called "catalog sample", please go and checkout this picture and see what kind of feeling I'm looking for. Please DO NOT just copy the catalog design from this sample. I'm just giving you a feeling of the catalog I want.

Requirements
Must have
• one page must display 2~3 products, with bottles pics, supplement fact table, text area for description.
• professional looking, neat and clean displays
• easy to read fond, size text
• good layout between bottles pics, supplement fact tables, texts and herbal images
Nice to have
• high quality, copyright-free herbs, greens, flowers, plants images associated with co-related products to decorate the catalog
Should not have
• must NOT be overly messy and hard-to-read

```html
<!DOCTYPE html>
<html lang="en">
<head>
<meta charset="utf-8">
<title>Verdalis Catalog</title>
<link href="https://fonts.googleapis.com/css2?family=Montserrat:wght@400;500;600;700&display=swap" rel="stylesheet">
<style>
  :root{
    --bg:#2a2a2a;
    --paper:#ffffff;
    --leaf:#8cc63f;
    --leaf-deep:#5a9a1e;
    --lime:#c8e86a;
    --brown:#4a2a12;
    --brown-mid:#5c3518;
    --ink:#3a3a3a;
    --bottle:#1f4d2c;
    --bottle-hi:#3a7a45;
  }
  *{margin:0;padding:0;box-sizing:border-box}
  html,body{width:1200px;height:1200px;overflow:hidden;background:var(--bg);font-family:'Montserrat',sans-serif;color:var(--ink)}
  .spread{position:absolute;left:205px;width:790px;height:560px;display:flex;box-shadow:0 10px 30px rgba(0,0,0,.5)}
  .spread--outer{top:25px}
  .spread--inner{top:615px}
  .page{position:relative;width:395px;height:560px;overflow:hidden;background:var(--paper)}
  .page__art{position:absolute;inset:0}
  .page--green{background:linear-gradient(160deg,#f6fbe9 0%,#d9f09a 45%,#9bd43c 100%)}
  .page--spine{border-left:8px solid var(--brown)}
  .products{position:absolute;left:14px;right:16px;display:flex;flex-direction:column}
  .product{display:flex;gap:12px;align-items:flex-start}
  .bottle{flex:none;width:40px;height:70px;margin-top:8px;border-radius:7px 7px 5px 5px;
    background:linear-gradient(90deg,var(--bottle) 0%,var(--bottle-hi) 45%,var(--bottle) 100%);position:relative}
  .bottle::before{content:"";position:absolute;left:7px;right:7px;top:-8px;height:10px;border-radius:3px 3px 0 0;background:var(--bottle)}
  .product__body{flex:1}
  .product__name{display:inline-block;background:var(--leaf);color:#fff;font-weight:700;font-size:10px;letter-spacing:.3px;
    padding:3px 12px 3px 8px;border-radius:0 12px 12px 0;margin-bottom:4px}
  .product__text{font-size:7.6px;line-height:1.38}
  .product__text b{font-weight:700;color:#222}
  .brand{position:absolute;left:0;right:0;top:395px;text-align:center}
  .brand__name{display:inline-flex;align-items:center;gap:8px;font-weight:500;font-size:44px;color:var(--leaf-deep);letter-spacing:-.5px}
  .brand__dot{width:10px;height:10px;border-radius:50%;background:var(--leaf)}
  .brand__tag{font-size:12px;color:var(--brown-mid);font-weight:600;margin-top:2px;padding-left:90px}
</style>
</head>
<body>

<!-- Outer spread: product page + cover -->
<section class="spread spread--outer">
  <article class="page">
    <svg class="page__art" width="395" height="560" viewBox="0 0 395 560">
      <defs>
        <linearGradient id="leafPhotoA" x1="0" y1="0" x2="1" y2="1">
          <stop offset="0" stop-color="#d7ee8a"/><stop offset=".5" stop-color="#7fbf2a"/><stop offset="1" stop-color="#2f6a14"/>
        </linearGradient>
      </defs>
      <circle cx="470" cy="-80" r="363" fill="var(--brown)"/>
      <circle cx="478" cy="-88" r="350" fill="url(#leafPhotoA)" role="img" aria-label="Photo of fresh green tea leaf shoots"/>
    </svg>
    <div class="products" style="top:280px;gap:14px">
      <div class="product">
        <div class="bottle" role="img" aria-label="Supplement bottle"></div>
        <div class="product__body">
          <span class="product__name">BITTER MELON</span>
          <p class="product__text">Lorem Ipsum is simply dummy text of the printing and typesetting industry, ever since the 1500s.<br><b>Pack size:</b> 60 veg capsules<br><b>Adult Dosage:</b> Lorem Ipsum is simply dummy text of the printing and typesetting industry.<br><b>Storage:</b> Store in a cool, dry place after opening.<br><b>Warnings:</b> For adults only. Consult physician if pregnant/lactating, taking medication or have a medical condition.</p>
        </div>
      </div>
      <div class="product">
        <div class="bottle" role="img" aria-label="Supplement bottle"></div>
        <div class="product__body">
          <span class="product__name">BRAIN BOOSTER</span>
          <p class="product__text">Lorem Ipsum is simply dummy text of the printing and typesetting industry. Lorem Ipsum has been the industry's standard dummy text ever since the 1500s.<br><b>Pack size:</b> 60 veg capsules<br><b>Adult Dosage:</b> Lorem Ipsum is simply dummy text of the printing and typesetting industry.<br><b>Storage:</b> Store in a cool, dry place after opening.<br><b>Warnings:</b> For adults only. Consult physician if pregnant/lactating, taking medication or have a medical condition.</p>
        </div>
      </div>
    </div>
  </article>

  <article class="page">
    <svg class="page__art" width="395" height="560" viewBox="0 0 395 560">
      <defs>
        <linearGradient id="leafPhotoB" x1="0" y1="1" x2="1" y2="0">
          <stop offset="0" stop-color="#2f6a14"/><stop offset=".45" stop-color="#86c232"/><stop offset="1" stop-color="#eef8d4"/>
        </linearGradient>
      </defs>
      <rect width="395" height="560" fill="url(#leafPhotoB)" role="img" aria-label="Photo of green tea plantation leaves"/>
      <path d="M-20 0 Q120 140 395 170 L395 185 Q110 160 -20 10 Z" fill="var(--leaf)"/>
      <path d="M-20 -10 Q120 130 395 160 L395 170 Q120 140 -20 0 Z" fill="#ffffff"/>
      <path d="M0 330 Q170 300 290 230 Q360 190 395 175 L395 560 L0 560 Z" fill="var(--brown)"/>
      <path d="M0 360 Q210 320 330 370 Q370 390 395 420 L395 560 L0 560 Z" fill="var(--paper)"/>
      <path d="M300 350 Q370 380 385 470 Q392 520 380 560 L395 560 L395 400 Q365 355 300 350 Z" fill="var(--leaf)"/>
    </svg>
    <div class="brand">
      <div class="brand__name"><span class="brand__dot"></span>Verdalis</div>
      <div class="brand__tag">Natural Nutrition</div>
    </div>
  </article>
</section>

<!-- Inner spread: product listings -->
<section class="spread spread--inner">
  <article class="page page--spine">
    <div class="products" style="top:12px;gap:10px">
      <div class="product">
        <div class="bottle" role="img" aria-label="Supplement bottle"></div>
        <div class="product__body">
          <span class="product__name">GREEN TEA EXTRACT</span>
          <p class="product__text">Lorem Ipsum is simply dummy text of the printing and typesetting industry. Lorem Ipsum has been the industry's standard dummy text ever since the 1500s.<br><b>Pack size:</b> 60 veg capsules<br><b>Adult Dosage:</b> Lorem Ipsum is simply dummy text of the printing and typesetting industry.<br><b>Storage:</b> Store in a cool, dry place after opening.<br><b>Warnings:</b> For adults only. Consult physician if pregnant/lactating, taking medication or have a medical condition.</p>
        </div>
      </div>
      <div class="product">
        <div class="bottle" role="img" aria-label="Supplement bottle"></div>
        <div class="product__body">
          <span class="product__name">GARCINIA CAMBOGIA+TURMERIC</span>
          <p class="product__text">Lorem Ipsum is simply dummy text of the printing and typesetting industry. Lorem Ipsum has been the industry's standard dummy text ever since the 1500s.<br><b>Pack size:</b> 60 veg capsules<br><b>Adult Dosage:</b> Lorem Ipsum is simply dummy text of the printing and typesetting industry.<br><b>Storage:</b> Store in a cool, dry place after opening.<br><b>Warnings:</b> For adults only. Consult physician if pregnant/lactating, taking medication or have a medical condition.</p>
        </div>
      </div>
      <div class="product">
        <div class="bottle" role="img" aria-label="Supplement bottle"></div>
        <div class="product__body">
          <span class="product__name">TURMERIC ENERGY</span>
          <p class="product__text">Lorem Ipsum is simply dummy text of the printing and typesetting industry. Lorem Ipsum has been the industry's standard dummy text ever since the 1500s.<br><b>Pack size:</b> 60 veg capsules<br><b>Adult Dosage:</b> Lorem Ipsum is simply dummy text of the printing and typesetting industry.<br><b>Storage:</b> Store in a cool, dry place after opening.<br><b>Warnings:</b> For adults only. Consult physician if pregnant/lactating, taking medication or have a medical condition.</p>
        </div>
      </div>
      <div class="product">
        <div class="bottle" role="img" aria-label="Supplement bottle"></div>
        <div class="product__body">
          <span class="product__name">CRANBERRY</span>
          <p class="product__text">Lorem Ipsum is simply dummy text of the printing and typesetting industry. Lorem Ipsum has been the industry's standard dummy text ever since the 1500s.<br><b>Pack size:</b> 60 veg capsules<br><b>Adult Dosage:</b> Lorem Ipsum is simply dummy text of the printing and typesetting industry.<br><b>Storage:</b> Store in a cool, dry place after opening.<br><b>Warnings:</b> For adults only. Consult physician if pregnant/lactating.</p>
        </div>
      </div>
    </div>
  </article>

  <article class="page page--green" role="img" aria-label="Soft green page with faint leaf photo">
    <div class="products" style="top:12px;gap:10px">
      <div class="product">
        <div class="bottle" role="img" aria-label="Supplement bottle"></div>
        <div class="product__body">
          <span class="product__name">GREEN VITALITY</span>
          <p class="product__text">Lorem Ipsum is simply dummy text of the printing and typesetting industry. Lorem Ipsum has been the industry's standard dummy text ever since the 1500s.<br><b>Pack size:</b> 60 veg capsules<br><b>Adult Dosage:</b> Lorem Ipsum is simply dummy text of the printing and typesetting industry.<br><b>Storage:</b> Store in a cool, dry place after opening.<br><b>Warnings:</b> For adults only. Consult physician if pregnant/lactating, taking medication or have a medical condition.</p>
        </div>
      </div>
      <div class="product">
        <div class="bottle" role="img" aria-label="Supplement bottle"></div>
        <div class="product__body">
          <span class="product__name">BRAIN BOOSTER</span>
          <p class="product__text">Lorem Ipsum is simply dummy text of the printing and typesetting industry. Lorem Ipsum has been the industry's standard dummy text ever since the 1500s.<br><b>Pack size:</b> 60 veg capsules<br><b>Adult Dosage:</b> Lorem Ipsum is simply dummy text of the printing and typesetting industry.<br><b>Storage:</b> Store in a cool, dry place after opening.<br><b>Warnings:</b> For adults only. Consult physician if pregnant/lactating, taking medication or have a medical condition.</p>
        </div>
      </div>
      <div class="product">
        <div class="bottle" role="img" aria-label="Supplement bottle"></div>
        <div class="product__body">
          <span class="product__name">NONI RESVERATROL</span>
          <p class="product__text">Lorem Ipsum is simply dummy text of the printing and typesetting industry. Lorem Ipsum has been the industry's standard dummy text ever since the 1500s.<br><b>Pack size:</b> 60 veg capsules<br><b>Adult Dosage:</b> Lorem Ipsum is simply dummy text of the printing and typesetting industry.<br><b>Storage:</b> Store in a cool, dry place after opening.<br><b>Warnings:</b> For adults only. Consult physician if pregnant/lactating, taking medication or have a medical condition.</p>
        </div>
      </div>
      <div class="product">
        <div class="bottle" role="img" aria-label="Supplement bottle"></div>
        <div class="product__body">
          <span class="product__name">LONGEVITY FORMAL</span>
          <p class="product__text">Lorem Ipsum is simply dummy text of the printing and typesetting industry. Lorem Ipsum has been the industry's standard dummy text ever since the 1500s.<br><b>Pack size:</b> 60 veg capsules<br><b>Adult Dosage:</b> Lorem Ipsum is simply dummy text of the printing and typesetting industry.<br><b>Storage:</b> Store in a cool, dry place after opening.<br><b>Warnings:</b> For adults only. Consult physician if pregnant/lactating.</p>
        </div>
      </div>
    </div>
  </article>
</section>

</body>
</html>
```